Save the Date card

This will be a Save the Date 5x7 card...preferably Hunter Green background

Annual Fund Leadership Dinner
June 20, 2023. 6:30 pm
Location: The Pellimore's Home
4187 Brindlecove Ridge Rd
Harrison, TN 37598

Other side of card:
We would prayerfully ask that you consider partnering with us as we kick off our Annual Fund this Fall to celebrate our 25 year anniversary as an Academy.
Please direct any questions to Marla Quenby, our Director of Advancement 423-555-0184 x 3617 or advancement@corvellanprep.org

```html
<!DOCTYPE html>
<html lang="en">
<head>
<meta charset="utf-8">
<title>Annual Fund Leadership Dinner – Save the Date</title>
<link rel="stylesheet" href="https://fonts.googleapis.com/css2?family=Cinzel:wght@400;600&family=Figtree:wght@400;500;700&display=swap">
<style>
  :root {
    --hunter: #1f3a23;
    --hunter-deep: #18301c;
    --cream: #efefe6;
    --gold: #a99a5a;
    --gold-dark: #8c7e45;
    --grey-text: #6f6f6a;
    --backdrop: #d9d6cf;
    --white: #ffffff;
  }
  * { box-sizing: border-box; margin: 0; padding: 0; }
  html, body { width: 1200px; height: 900px; overflow: hidden; }
  body {
    background: var(--backdrop);
    font-family: "Figtree", Arial, sans-serif;
    display: flex;
    align-items: center;
    justify-content: center;
    gap: 24px;
  }
  .card {
    position: relative;
    width: 570px;
    height: 407px;
    overflow: hidden;
    box-shadow: 0 6px 18px rgba(0,0,0,0.18);
  }
  .card-art { position: absolute; inset: 0; }
  .card-layer { position: absolute; left: 0; width: 100%; text-align: center; }

  /* front */
  .card--front { background: var(--cream); }
  .wordmark {
    font-family: "Cinzel", Georgia, serif;
    font-weight: 600;
    color: var(--hunter);
    letter-spacing: 1px;
  }
  .wordmark--front {
    position: absolute; left: 176px; top: 150px;
    font-size: 21px; color: var(--cream);
  }
  .event-kicker {
    top: 246px;
    font-family: "Cinzel", Georgia, serif;
    font-size: 24px; color: var(--hunter); letter-spacing: 1px;
  }
  .event-title {
    top: 271px;
    font-family: "Cinzel", Georgia, serif;
    font-weight: 600; font-size: 39px; color: var(--hunter); letter-spacing: 1px;
  }
  .event-date {
    top: 326px;
    font-size: 15px; font-weight: 500; color: var(--white); letter-spacing: 0.5px;
  }
  .event-host { top: 358px; font-size: 14px; color: var(--hunter); }
  .event-address { top: 377px; font-size: 13.5px; color: var(--grey-text); }

  /* back */
  .card--back { background: var(--hunter); }
  .wordmark--back { top: 30px; font-size: 22px; }
  .appeal {
    top: 148px; padding: 0 70px;
    font-size: 15px; line-height: 1.55; color: var(--white);
  }
  .appeal-highlight {
    display: block;
    font-family: "Cinzel", Georgia, serif;
    font-size: 22px; color: var(--gold); line-height: 1.3; letter-spacing: 0.5px;
  }
  .contact {
    top: 268px;
    font-size: 12.5px; line-height: 1.55; color: var(--gold);
  }
  .contact strong { font-weight: 700; }
  .website {
    top: 341px;
    font-size: 14px; color: var(--white); letter-spacing: 2.5px;
  }
</style>
</head>
<body>

  <section class="card card--front" aria-label="Front of save the date card">
    <svg class="card-art" width="570" height="407" viewBox="0 0 570 407">
      <defs>
        <linearGradient id="campus-tone" x1="0" y1="0" x2="1" y2="1">
          <stop offset="0" stop-color="#3a4f2e"/>
          <stop offset="0.55" stop-color="#4a5a42"/>
          <stop offset="1" stop-color="#2f4530"/>
        </linearGradient>
      </defs>
      <path class="campus-photo" role="img" aria-label="Aerial photograph of the school campus with a green tint"
            d="M0,0 H570 V140 L260,236 L0,258 Z" fill="url(#campus-tone)"/>
      <path class="photo-band" d="M110,250 L260,226 L470,152 L462,166 L262,240 L118,258 Z" fill="var(--gold)"/>
      <rect class="ribbon-fold" x="80" y="330" width="22" height="22" fill="var(--gold-dark)"/>
      <rect class="ribbon-fold" x="468" y="318" width="22" height="22" fill="var(--gold-dark)"/>
      <rect class="date-ribbon" x="92" y="322" width="386" height="26" fill="var(--gold)"/>
    </svg>
    <div class="wordmark wordmark--front">Corvellan Prep</div>
    <p class="card-layer event-kicker">Annual Fund</p>
    <h1 class="card-layer event-title">Leadership Dinner</h1>
    <p class="card-layer event-date">TUESDAY, JUNE 20, 2023. 6:30 PM</p>
    <p class="card-layer event-host">The Pellimore's Home</p>
    <p class="card-layer event-address">4187 Brindlecove Ridge Rd Harrison, TN 37598</p>
  </section>

  <section class="card card--back" aria-label="Back of save the date card">
    <svg class="card-art" width="570" height="407" viewBox="0 0 570 407">
      <path class="cream-cap" d="M0,0 H570 V58 Q300,112 0,100 Z" fill="var(--cream)"/>
      <path class="cap-band" d="M115,98 L285,82 L480,50 L472,62 L287,94 L122,106 Z" fill="var(--gold)"/>
      <rect class="divider" x="255" y="252" width="60" height="2" fill="var(--gold)"/>
      <rect class="ribbon-fold" x="112" y="344" width="22" height="22" fill="var(--gold-dark)"/>
      <rect class="ribbon-fold" x="436" y="334" width="22" height="22" fill="var(--gold-dark)"/>
      <rect class="web-ribbon" x="124" y="336" width="322" height="26" fill="var(--gold)"/>
    </svg>
    <div class="card-layer wordmark wordmark--back">Corvellan Prep</div>
    <p class="card-layer appeal">
      We would prayerfully ask that you consider partnering with us as we kick off our Annual Fund this Fall to celebrate our
      <span class="appeal-highlight">25 Year Anniversary</span>
      as an Academy.
    </p>
    <p class="card-layer contact">
      Please direct any questions to Marla Quenby, our Director of Advancement<br>
      <strong>423-555-0184 x 3617 or advancement@corvellanprep.org</strong>
    </p>
    <p class="card-layer website">www.corvellanprep.org</p>
  </section>

</body>
</html>
```